Email signature banner for companys 60th anniversary

We are a transportation company. This is what our website people came up with so far:

https://www.plavemockups.com/design/8xWq2LpZr4TnBv7KcYdMfA/Bornel?node-id=4417-35

I want a picture of our transport truck with the decal on the back that we are putting on it.

Our website is www.bornel.com

Target Market(s)

Customer recognition

Industry/Entity Type

fuel and oil distribution company

Requirements
Must have
• our 60th anniversary logo
Nice to have
• Delivering Energy to Build Communites.
Should not have
• picture of the guy from the current banner provided

```html
<!DOCTYPE html>
<html lang="en">
<head>
<meta charset="utf-8">
<title>Celebrating 60 Years – Email Signature Banners</title>
<link rel="stylesheet" href="https://fonts.googleapis.com/css2?family=Bebas+Neue&family=Russo+One&display=swap">
<style>
  :root {
    --navy: #1f3872;
    --red: #d0252b;
    --sky: #4f8ac9;
    --white: #ffffff;
    --stripe-navy: #5b86c6;
    --stripe-red: #8fa7d6;
  }
  html, body {
    margin: 0;
    padding: 0;
    width: 1200px;
    height: 1200px;
    overflow: hidden;
    background: var(--white);
  }
  .canvas {
    position: relative;
    width: 1200px;
    height: 1200px;
  }
  .banner {
    position: absolute;
    left: 69px;
    width: 1070px;
    height: 269px;
    display: block;
  }
  .banner--navy { top: 280px; }
  .banner--red { top: 619px; }
  .label-small {
    font-family: "Bebas Neue", "Oswald", sans-serif;
  }
  .label-number {
    font-family: "Russo One", "Arial Black", sans-serif;
  }
</style>
</head>
<body>
<main class="canvas">

  <!-- Navy variant -->
  <svg class="banner banner--navy" viewBox="0 0 1070 269" aria-label="Celebrating 60 years">
    <defs>
      <linearGradient id="stripeFadeNavy" x1="0" x2="1" y1="0" y2="0">
        <stop offset="0" stop-color="var(--stripe-navy)" stop-opacity="1"/>
        <stop offset="1" stop-color="var(--stripe-navy)" stop-opacity="0"/>
      </linearGradient>
      <linearGradient id="truckNavy" x1="0" x2="1" y1="0" y2="1">
        <stop offset="0" stop-color="#e4e6ea"/>
        <stop offset="0.6" stop-color="#b9bdc4"/>
        <stop offset="1" stop-color="#3a3f48"/>
      </linearGradient>
    </defs>
    <rect class="banner-bg" width="1070" height="269" fill="var(--navy)"/>
    <g class="speed-stripes" fill="url(#stripeFadeNavy)">
      <rect x="0" y="14" width="430" height="7"/>
      <rect x="0" y="36" width="430" height="7"/>
      <rect x="0" y="58" width="430" height="7"/>
      <rect x="0" y="80" width="420" height="7"/>
      <rect x="0" y="102" width="400" height="7"/>
      <rect x="0" y="124" width="380" height="7"/>
      <rect x="0" y="146" width="360" height="7"/>
    </g>
    <path class="accent-panel" d="M887 0 L955 68 Q1015 130 1012 186 Q1010 232 969 269 L1070 269 L1070 0 Z" fill="var(--red)"/>
    <path class="accent-edge" d="M887 0 L955 68 Q1015 130 1012 186 Q1010 232 969 269" fill="none" stroke="var(--sky)" stroke-width="3"/>
    <rect class="truck-illustration" role="img" aria-label="Illustration of a white fuel tanker truck seen from the rear, with the 60th anniversary decal on the tank" x="15" y="7" width="345" height="244" rx="36" fill="url(#truckNavy)" opacity="0.9"/>
    <text class="label-small" x="441" y="79" font-size="71" fill="var(--white)" textLength="454" lengthAdjust="spacing">CELEBRATING</text>
    <text class="label-number" x="439" y="245" font-size="226" fill="var(--white)" textLength="397" lengthAdjust="spacingAndGlyphs">60</text>
    <text class="label-small" transform="translate(857 98) rotate(90)" font-size="74" fill="var(--white)" textLength="144" lengthAdjust="spacingAndGlyphs">YEARS</text>
  </svg>

  <!-- Red variant -->
  <svg class="banner banner--red" viewBox="0 0 1070 269" aria-label="Celebrating 60 years">
    <defs>
      <linearGradient id="stripeFadeRed" x1="0" x2="1" y1="0" y2="0">
        <stop offset="0" stop-color="var(--stripe-red)" stop-opacity="1"/>
        <stop offset="1" stop-color="var(--stripe-red)" stop-opacity="0"/>
      </linearGradient>
      <linearGradient id="truckRed" x1="0" x2="1" y1="0" y2="1">
        <stop offset="0" stop-color="#e4e6ea"/>
        <stop offset="0.6" stop-color="#b9bdc4"/>
        <stop offset="1" stop-color="#3a3f48"/>
      </linearGradient>
    </defs>
    <rect class="banner-bg" width="1070" height="269" fill="var(--red)"/>
    <g class="speed-stripes" fill="url(#stripeFadeRed)">
      <rect x="0" y="14" width="430" height="7"/>
      <rect x="0" y="36" width="430" height="7"/>
      <rect x="0" y="58" width="430" height="7"/>
      <rect x="0" y="80" width="410" height="7"/>
      <rect x="0" y="102" width="395" height="7"/>
      <rect x="0" y="124" width="380" height="7"/>
      <rect x="0" y="146" width="360" height="7"/>
    </g>
    <path class="accent-panel" d="M514 0 L462 52 Q390 125 387 160 Q385 215 431 269 L1070 269 L1070 0 Z" fill="var(--sky)"/>
    <path class="accent-edge" d="M514 0 L462 52 Q390 125 387 160 Q385 215 431 269" fill="none" stroke="var(--navy)" stroke-width="3"/>
    <rect class="edge-strip" x="1040" y="0" width="30" height="269" fill="var(--navy)"/>
    <rect class="truck-illustration" role="img" aria-label="Illustration of a white fuel tanker truck seen from the rear, with the 60th anniversary decal on the tank" x="15" y="7" width="345" height="244" rx="36" fill="url(#truckRed)" opacity="0.9"/>
    <text class="label-small" x="522" y="81" font-size="71" fill="var(--navy)" textLength="452" lengthAdjust="spacing">CELEBRATING</text>
    <text class="label-number" x="521" y="244" font-size="224" fill="var(--navy)" textLength="394" lengthAdjust="spacingAndGlyphs">60</text>
    <text class="label-small" transform="translate(938 100) rotate(90)" font-size="73" fill="var(--navy)" textLength="143" lengthAdjust="spacingAndGlyphs">YEARS</text>
  </svg>

</main>
</body>
</html>
```